business stationery

have a gorgeous logo that needs to be incorporated on stationery. Was hoping to do something on letterhead that was a paper that looked like "bark" from a tree or something that resembled the "woods." Soft paper with some very basic natural elements. Same thing for business cards. Think American lakeside cabin. Organic. Natural. Calm and welcoming but clear to read and understand. Wanted to use alot of black.

Target Market(s)

buyers of Tobias Wrenfield home. Client that would have more than one home and in need of rare pieces and items to furnish an upmarket lakeside holiday cabin in the woods. Someone who treasures beautiful hand made items, organic foods and a real crackling fire but with money to burn in it!

Industry/Entity Type

Business

Requirements
Must have
• My logo
My business name
www.fernandcopper.example
Natural almost raw effect paper
My ABN: 62 307 514 928 (to be placed in small writing at the bottom of card/letterhead)
Nice to have
• The website will consist of a cabin door that you "open" with a creak sound effect and then you go "inside" to look at the various rooms to start shopping. Want to bring that element of texture and warmth into the stationary also.
Should not have
• Anything modern or hard to read items

```html
<!DOCTYPE html>
<html lang="en">
<head>
<meta charset="utf-8">
<title>Fern &amp; Copper — Business Stationery</title>
<link rel="stylesheet" href="https://fonts.googleapis.com/css2?family=Cabin:wght@400;600;700&display=swap">
<style>
  :root {
    --canvas: #ffffff;
    --wood-dark: #3b2416;
    --wood-mid: #6a4128;
    --wood-light: #8a5a38;
    --paper-light: #efe6d0;
    --paper-mid: #e2d5b6;
    --paper-edge: #cdbb93;
    --ink: #1a1410;
    --maroon: #7a1e1a;
    --card-black: #0c0b0a;
    --white: #ffffff;
  }
  * { box-sizing: border-box; margin: 0; padding: 0; }
  html, body { width: 1200px; height: 1200px; overflow: hidden; background: var(--canvas); }
  body { position: relative; font-family: "Cabin", "Trebuchet MS", sans-serif; color: var(--ink); }

  .abs { position: absolute; }
  .wood {
    position: absolute;
    background:
      repeating-linear-gradient(180deg, rgba(0,0,0,.28) 0 2px, transparent 2px 58px),
      linear-gradient(90deg, var(--wood-dark), var(--wood-mid) 30%, var(--wood-light) 50%, var(--wood-mid) 72%, var(--wood-dark));
  }
  .paper {
    position: absolute;
    background: radial-gradient(ellipse at 45% 40%, var(--paper-light), var(--paper-mid) 70%, var(--paper-edge));
  }
  .brand { position: absolute; display: flex; justify-content: center; align-items: center; gap: 7px; line-height: 1; white-space: nowrap; }
  .brand-dot { width: 12px; height: 12px; border-radius: 50%; background: var(--maroon); flex: none; }
  .brand-name { font-weight: 700; text-transform: uppercase; color: var(--ink); }
  .web { position: absolute; color: var(--maroon); font-weight: 600; line-height: 1; white-space: nowrap; }

  /* Letterhead */
  .letterhead-wood { left: 71px; top: 56px; width: 818px; height: 1056px; }
  .letterhead-paper { left: 100px; top: 93px; width: 753px; height: 994px; border-radius: 6px 14px 4px 18px; }
  .letterhead-brand { left: 0; width: 934px; top: 190px; }
  .letterhead-brand .brand-name { font-size: 34px; }
  .letterhead-web { left: 0; width: 960px; text-align: center; top: 240px; font-size: 14px; }
  .letterhead-footer { left: 213px; top: 1041px; font-size: 17px; font-weight: 600; line-height: 1; white-space: nowrap; }

  /* Envelope */
  .envelope { position: absolute; left: 444px; top: 307px; width: 716px; height: 312px; overflow: hidden; box-shadow: 0 2px 6px rgba(0,0,0,.25); }
  .envelope .paper { inset: 0; }
  .envelope-band { left: 0; right: 0; bottom: 0; height: 31px; }
  .envelope-brand { right: 29px; top: 70px; }
  .envelope-brand .brand-name { font-size: 26px; }
  .envelope-brand .brand-dot { width: 10px; height: 10px; }
  .envelope-web { right: 37px; top: 110px; font-size: 12px; }
  .sender-name { left: 12px; top: 206px; color: var(--maroon); font-size: 19px; line-height: 1; }
  .sender-address { left: 12px; top: 228px; font-size: 10px; line-height: 14px; }
  .sender-contact { left: 12px; top: 262px; font-size: 12px; font-weight: 600; line-height: 1; white-space: nowrap; }
  .envelope-abn { right: 7px; top: 266px; font-size: 9px; line-height: 1; }

  /* Business card front */
  .card-front-wood { left: 484px; top: 644px; width: 243px; height: 137px; }
  .card-front-paper { left: 500px; top: 653px; width: 213px; height: 120px; border-radius: 4px 10px 6px 12px; }
  .card-front-brand { left: 500px; width: 213px; top: 717px; gap: 5px; }
  .card-front-brand .brand-name { font-size: 18px; }
  .card-front-brand .brand-dot { width: 8px; height: 8px; }

  /* Business card back */
  .card-back { position: absolute; left: 483px; top: 801px; width: 242px; height: 132px; background: var(--card-black); color: var(--white); text-align: center; }
  .card-back p { position: absolute; left: 0; width: 100%; line-height: 1; white-space: nowrap; }
  .card-back-name { top: 20px; color: var(--maroon); font-size: 15px; }
  .card-back-address { top: 38px; font-size: 8px; }
  .card-back-phone { top: 59px; font-size: 10px; }
  .card-back-email { top: 72px; font-size: 10px; }
  .card-back-web { top: 85px; font-size: 10px; }
  .card-back-web .accent { color: var(--maroon); }
  .card-back p.card-back-abn { left: auto; right: 12px; width: auto; top: 116px; font-size: 7px; }
</style>
</head>
<body>

  <div class="letterhead-wood wood" role="img" aria-label="Dark wood plank background"></div>
  <div class="letterhead-paper paper" role="img" aria-label="Aged, torn parchment paper texture"></div>
  <div class="brand letterhead-brand"><span class="brand-dot"></span><span class="brand-name">Fern &amp; Copper</span></div>
  <p class="web letterhead-web">www.fernandcopper.example</p>
  <p class="abs letterhead-footer">Ph: 555-014-2286 | E-mail: Hollis@fernandcopper.example</p>

  <section class="envelope">
    <div class="paper" role="img" aria-label="Aged parchment paper texture"></div>
    <div class="wood envelope-band" role="img" aria-label="Dark wood strip"></div>
    <div class="brand envelope-brand"><span class="brand-dot"></span><span class="brand-name">Fern &amp; Copper</span></div>
    <p class="web envelope-web">www.fernandcopper.example</p>
    <p class="abs sender-name">Hollis Ardane</p>
    <p class="abs sender-address">D-112, Cedar Row, Larchmere Park<br>Lakeside-400921</p>
    <p class="abs sender-contact">Ph: 555-014-2286 | E-mail: Hollis@fernandcopper.example</p>
    <p class="abs envelope-abn">ABN: 62 307 514 928</p>
  </section>

  <div class="card-front-wood wood" role="img" aria-label="Dark wood background"></div>
  <div class="card-front-paper paper" role="img" aria-label="Torn parchment paper texture"></div>
  <div class="brand card-front-brand"><span class="brand-dot"></span><span class="brand-name">Fern &amp; Copper</span></div>

  <section class="card-back">
    <p class="card-back-name">Hollis Ardane</p>
    <p class="card-back-address">D-112, Cedar Row, Larchmere Park, Lakeside-400921</p>
    <p class="card-back-phone">Ph: 555-014-2286</p>
    <p class="card-back-email">E-mail: Hollis@fernandcopper.example</p>
    <p class="card-back-web">www.<span class="accent">fernandcopper</span>.example</p>
    <p class="card-back-abn">ABN: 62 307 514 928</p>
  </section>

</body>
</html>
```